Hydraulics Company Business Card Design

Modern business card design for a hydraulics company.
Our company colours are - black, orange and white.
I would like the following contact details included-
Name
Position
Phone number
Email
Website
Street Address

I have attached our company logo.
I would like the back of the card white.

Thank you.

```html
<!DOCTYPE html>
<html lang="en">
<head>
<meta charset="utf-8">
<title>Ridgeway Hydraulics – Business Card</title>
<link href="https://fonts.googleapis.com/css2?family=Montserrat:wght@400;700&family=Quicksand:wght@400;500&display=swap" rel="stylesheet">
<style>
  :root {
    --stage: #ddd7cd;
    --card-dark: #070505;
    --card-light: #ffffff;
    --orange: #f39a1e;
    --white: #ffffff;
    --ink: #1a1614;
    --band: #2a1a08;
  }
  html, body {
    margin: 0;
    padding: 0;
    overflow: hidden;
  }
  body {
    width: 1200px;
    height: 900px;
    background: var(--stage);
    position: relative;
  }
  .card {
    position: absolute;
    left: 320px;
    width: 560px;
    height: 320px;
    border-radius: 44px;
    overflow: hidden;
    box-shadow: 0 10px 28px rgba(0,0,0,0.22);
  }
  .card--logo-side {
    top: 70px;
    background: var(--card-light);
  }
  .card--info-side {
    top: 500px;
    background: var(--card-dark);
  }

  .brand-name {
    font-family: "Montserrat", sans-serif;
    font-weight: 700;
    color: var(--orange);
    margin: 0;
    line-height: 1;
    white-space: nowrap;
  }
  .card--logo-side .brand-name {
    position: absolute;
    left: 0;
    right: 0;
    top: 118px;
    text-align: center;
    font-size: 44px;
  }
  .site-url {
    position: absolute;
    left: 0;
    right: 0;
    bottom: 46px;
    margin: 0;
    text-align: center;
    font-family: "Quicksand", sans-serif;
    font-weight: 500;
    font-size: 11px;
    letter-spacing: 3px;
    color: var(--ink);
  }
  .site-url span { color: var(--orange); }

  .info-band {
    position: absolute;
    inset: 0;
  }
  .person {
    position: absolute;
    left: 30px;
    top: 82px;
  }
  .person-name {
    font-family: "Montserrat", sans-serif;
    font-weight: 700;
    font-size: 14px;
    color: var(--orange);
    text-transform: uppercase;
    margin: 0;
  }
  .person-role {
    font-family: "Quicksand", sans-serif;
    font-size: 14px;
    color: var(--white);
    margin: 2px 0 0;
  }
  .contact-list {
    position: absolute;
    right: 34px;
    top: 102px;
    margin: 0;
    padding: 0;
    list-style: none;
    font-family: "Quicksand", sans-serif;
    font-size: 13px;
    color: var(--white);
    text-align: right;
  }
  .contact-list li {
    display: flex;
    justify-content: flex-end;
    align-items: center;
    gap: 8px;
    height: 21px;
  }
  .contact-list svg { width: 14px; height: 14px; flex: none; }
  .info-rule {
    position: absolute;
    right: 34px;
    top: 198px;
    width: 270px;
    height: 1px;
    background: var(--orange);
  }
  .card--info-side .brand-name {
    position: absolute;
    right: 34px;
    top: 220px;
    font-size: 32px;
  }
</style>
</head>
<body>

<section class="card card--logo-side" aria-label="Card back">
  <p class="brand-name">Ridgeway Hydraulics</p>
  <p class="site-url">www.<span>ridgewayhydraulics</span>.com.au</p>
</section>

<section class="card card--info-side" aria-label="Card front">
  <svg class="info-band" viewBox="0 0 560 320" aria-hidden="true">
    <path d="M0 60 L100 60 Q118 60 128 70 Q138 80 156 80 L560 80"
          fill="none" stroke="var(--band)" stroke-width="14"/>
  </svg>

  <div class="person">
    <p class="person-name">Daniel Moreau</p>
    <p class="person-role">Owner</p>
  </div>

  <ul class="contact-list">
    <li>0240001234
      <svg viewBox="0 0 24 24"><path fill="var(--orange)" d="M6.6 10.8a15 15 0 0 0 6.6 6.6l2.2-2.2a1 1 0 0 1 1-.25 11.4 11.4 0 0 0 3.6.57 1 1 0 0 1 1 1V20a1 1 0 0 1-1 1A17 17 0 0 1 3 4a1 1 0 0 1 1-1h3.5a1 1 0 0 1 1 1c0 1.25.2 2.45.57 3.6a1 1 0 0 1-.25 1z"/></svg>
    </li>
    <li>18 Carter Rd, Millbrook NSW 2700
      <svg viewBox="0 0 24 24"><path fill="var(--orange)" d="M12 2a7 7 0 0 0-7 7c0 5.2 7 13 7 13s7-7.8 7-13a7 7 0 0 0-7-7zm0 9.5A2.5 2.5 0 1 1 12 6.5a2.5 2.5 0 0 1 0 5z"/></svg>
    </li>
    <li>info@ridgewayhydraulics.com.au
      <svg viewBox="0 0 24 24"><rect x="2" y="5" width="20" height="14" rx="1" fill="none" stroke="var(--orange)" stroke-width="2"/><path d="M2 6l10 7 10-7" fill="none" stroke="var(--orange)" stroke-width="2"/></svg>
    </li>
    <li>www.ridgewayhydraulics.com.au
      <svg viewBox="0 0 24 24" fill="none" stroke="var(--orange)" stroke-width="1.8"><circle cx="12" cy="12" r="10"/><ellipse cx="12" cy="12" rx="4" ry="10"/><path d="M2 12h20M4 7h16M4 17h16"/></svg>
    </li>
  </ul>

  <div class="info-rule"></div>
  <p class="brand-name">Ridgeway Hydraulics</p>
</section>

</body>
</html>
```